Use responsive design to make this page look and behave awesome in any size

YOU CAN SUBMIT PSD, HOWEVER, THE WINNER MUST SUBMIT PROVIDE A SINGLE CODED PAGE PER THE LINK AND INSTRUCTIONS AT THE BOTTOM OF THIS BRIEF. While developing an internal website, we realized we are not super great at making things look awesome and responsive for phone/tablet/desktop. Thats where you come in. We want you to take this code, Fork it, and then make it look awesome and work great on any size device.

Task at hand:

This page is a simple dashboard showing how a number of stores stack up against each other and against a corporate goal.

Top: Goal title, and where the logged in person's store stands in the ranking.
Green means you are in compliance
Red means you are not in compliance

Middle: Description of goal. Words to describe what the corporate goal is, and a target number.

Bottom: Here we just want to show the top 10 and bottom 5 out of 100+ stores. if your in the top ten, you are highlighted. If your in the bottom 5, you will be highlighted there too. If you are in the middle, we would put the your store info between the top and bottom... indicating your in the middle.
Green means you they are in compliance
Red means they are not in compliance

Your Mission is not only to make this look fantastic and responsive, but to have usable code in there.

You don't need to do any logic. All we care about is look and feel and responsive behavior on different size browsers.

The winner obviously gets the prize, and hopefully can become a solid resource to do more of this type of thing for us in the future.

Instructions:
Go to this link: https://codequill.example/edit/tvx-leaderpanel-widget
Click on the blue Fork button. This will give you a new URL that you can paste back into the contest to review results for us to see your work.
Uploading pictures is not necessary as the responsive code is what is important here.

Good luck!

Number of Pages Required

1 page

Requirements
Must have
• The page must be responsive and look very professional AND game like.
Should not have
• plugins. just native code

```html
<!DOCTYPE html>
<html lang="en">
<head>
<meta charset="utf-8">
<title>Lead Measures</title>
<link rel="stylesheet" href="https://fonts.googleapis.com/css2?family=Poppins:wght@400;500&display=swap">
<style>
:root{
  --brand:#1b4c8c;
  --page:#f0f0f0;
  --card:#ffffff;
  --band:#f2f2f2;
  --line:#e6e6e6;
  --ink:#333333;
  --good:#2ea33a;
  --bad:#e8302c;
  --alert:#f3252f;
}
*{box-sizing:border-box;margin:0;padding:0}
html,body{width:1200px;height:3888px;overflow:hidden}
body{background:var(--page);font-family:'Poppins',sans-serif;color:var(--ink);position:relative}
.top-bar{position:absolute;left:0;top:0;width:1200px;height:78px;background:var(--brand);color:#fff;
  display:flex;align-items:center;justify-content:center;font-size:28px;font-weight:500;letter-spacing:.5px}
.measure{position:absolute;left:86px;width:1028px;background:var(--card);border:1px solid #dcdcdc;border-radius:4px;
  box-shadow:0 1px 4px rgba(0,0,0,.08)}
.measure-title{height:70px;display:flex;align-items:center;justify-content:center;font-size:34px;font-weight:400}
.measure-title .score{margin-left:12px}
.goal{height:78px;background:var(--band);border-top:1px solid var(--line);border-bottom:1px solid var(--line);
  display:flex;align-items:center;justify-content:center;font-size:22px}
.ranking{list-style:none;padding-top:13px}
.ranking li{display:flex;align-items:center;height:46.4px;font-size:17px;border-bottom:1px solid var(--line)}
.ranking li:last-child{border-bottom:none}
.rank{width:430px;padding-left:82px;color:var(--ink)}
.store{width:443px}
.value{flex:1}
.good{color:var(--good)}
.bad{color:var(--bad)}
.ranking li.mine{background:var(--alert)}
.ranking li.mine span{color:#fff}
.site-foot{position:absolute;left:0;top:3803px;width:1200px;height:85px;background:var(--brand);color:#fff;
  display:flex;align-items:center;justify-content:center;font-size:16px}
.site-foot .code{position:absolute;right:18px;bottom:14px;font-size:14px}
</style>
</head>
<body>
<header class="top-bar">LEAD MEASURES</header>

<section class="measure" style="top:124px;height:866px">
  <h2 class="measure-title">Team <span class="score good">92.1%</span></h2>
  <p class="goal">Use Slow Stock wherever possible &nbsp;-&nbsp; 80%</p>
  <ol class="ranking">
    <li><span class="rank">01</span><span class="store bad">(1) yjcQbtCyQu</span><span class="value bad">1%</span></li>
    <li><span class="rank">02</span><span class="store bad">(1) crsmlcfXwS</span><span class="value bad">1%</span></li>
    <li><span class="rank">03</span><span class="store bad">(2) wnlJojLRSf</span><span class="value bad">2%</span></li>
    <li><span class="rank">04</span><span class="store bad">(2) swEbjeRrpi</span><span class="value bad">2%</span></li>
    <li><span class="rank">05</span><span class="store bad">(4) oUauMPncOA</span><span class="value bad">4%</span></li>
    <li><span class="rank">06</span><span class="store bad">(5) vYufdHZExR</span><span class="value bad">5%</span></li>
    <li><span class="rank">07</span><span class="store bad">(5) jvBnNaGkeE</span><span class="value bad">5%</span></li>
    <li><span class="rank">08</span><span class="store bad">(6) CuWRvexCs</span><span class="value bad">6%</span></li>
    <li><span class="rank">09</span><span class="store bad">(7) XQFCUbSoko</span><span class="value bad">7%</span></li>
    <li><span class="rank">10</span><span class="store bad">(7) GucpFDVVJP</span><span class="value bad">7%</span></li>
    <li><span class="rank">96</span><span class="store good">(94) VoDGNkvwai</span><span class="value good">94%</span></li>
    <li><span class="rank">97</span><span class="store good">(94) IEjPTiBSih</span><span class="value good">94%</span></li>
    <li><span class="rank">98</span><span class="store good">(96) IWwFhTvkZb</span><span class="value good">96%</span></li>
    <li><span class="rank">99</span><span class="store good">(96) IzLCRXlLu</span><span class="value good">96%</span></li>
    <li><span class="rank">100</span><span class="store good">(96) pXPrzpcrUY</span><span class="value good">96%</span></li>
  </ol>
</section>

<section class="measure" style="top:1031px;height:863px">
  <h2 class="measure-title">Slow <span class="score good">0%</span></h2>
  <p class="goal">Less than 0% of inventory slower than 100 days &nbsp;-&nbsp; &lt; 1%</p>
  <ol class="ranking">
    <li><span class="rank">01</span><span class="store good">(89) NZBGVuimnc</span><span class="value good">0%</span></li>
    <li><span class="rank">02</span><span class="store good">(80) GaccDehKUO</span><span class="value good">0%</span></li>
    <li><span class="rank">03</span><span class="store good">(55) aPfpNcqcDh</span><span class="value good">0%</span></li>
    <li><span class="rank">04</span><span class="store good">(97) YqyVfKTTl</span><span class="value good">0%</span></li>
    <li><span class="rank">05</span><span class="store good">(67) PvQdqyeaHr</span><span class="value good">0%</span></li>
    <li class="mine"><span class="rank">06</span><span class="store">(00) Your Store</span><span class="value">2%</span></li>
    <li><span class="rank">07</span><span class="store bad">(40) jyMfVYlVbl</span><span class="value bad">2%</span></li>
    <li><span class="rank">08</span><span class="store bad">(11) QSESmpDJqw</span><span class="value bad">2%</span></li>
    <li><span class="rank">09</span><span class="store bad">(71) nIiaXFpJWv</span><span class="value bad">2%</span></li>
    <li><span class="rank">10</span><span class="store bad">(51) ENrkkveKpb</span><span class="value bad">2%</span></li>
    <li><span class="rank">96</span><span class="store bad">(90) VZgTUWgJTU</span><span class="value bad">8%</span></li>
    <li><span class="rank">97</span><span class="store bad">(67) nRGVsKcZhP</span><span class="value bad">9%</span></li>
    <li><span class="rank">98</span><span class="store bad">(32) JckeFPUVJV</span><span class="value bad">9%</span></li>
    <li><span class="rank">99</span><span class="store bad">(57) RxygcFNCRC</span><span class="value bad">9%</span></li>
    <li><span class="rank">100</span><span class="store bad">(20) MmydxeaOMu</span><span class="value bad">10%</span></li>
  </ol>
</section>

<section class="measure" style="top:1948px;height:863px">
  <h2 class="measure-title">Turns <span class="score good">2.2</span></h2>
  <p class="goal">Turn inventory 6 or more times a year &nbsp;-&nbsp; &gt; 6</p>
  <ol class="ranking">
    <li><span class="rank">01</span><span class="store bad">(8) VZaEOSVkef</span><span class="value bad">0.2</span></li>
    <li><span class="rank">02</span><span class="store bad">(3) PcVKNpUNmj</span><span class="value bad">0.2</span></li>
    <li><span class="rank">03</span><span class="store bad">(4) RIlyRZsTln</span><span class="value bad">0.4</span></li>
    <li><span class="rank">04</span><span class="store bad">(9) epINQFtERO</span><span class="value bad">0.6</span></li>
    <li><span class="rank">05</span><span class="store bad">(3) FbFOzkjSpF</span><span class="value bad">0.7</span></li>
    <li><span class="rank">06</span><span class="store bad">(7) RdzzkcVqtC</span><span class="value bad">0.8</span></li>
    <li><span class="rank">07</span><span class="store bad">(1) DiIlXiGkTx</span><span class="value bad">0.8</span></li>
    <li><span class="rank">08</span><span class="store bad">(1) jxWbwORyVa</span><span class="value bad">0.8</span></li>
    <li><span class="rank">09</span><span class="store bad">(4) UyzYflMzU</span><span class="value bad">0.8</span></li>
    <li><span class="rank">10</span><span class="store bad">(4) KVlgJQBgAc</span><span class="value bad">1</span></li>
    <li><span class="rank">96</span><span class="store good">(5) gBeGhPqZNF</span><span class="value good">9.7</span></li>
    <li><span class="rank">97</span><span class="store good">(8) gGhhZFlCHP</span><span class="value good">9.7</span></li>
    <li><span class="rank">98</span><span class="store good">(9) emavLKfhzN</span><span class="value good">9.8</span></li>
    <li><span class="rank">99</span><span class="store good">(7) PyuviZHBxH</span><span class="value good">9.8</span></li>
    <li><span class="rank">100</span><span class="store good">(5) LidsyctcWm</span><span class="value good">9.9</span></li>
  </ol>
</section>

<section class="measure" style="top:2862px;height:864px">
  <h2 class="measure-title">Values <span class="score good">1.9</span></h2>
  <p class="goal">Inventory Value to be around 1.25 x you last months INVENTORY sales &nbsp;-&nbsp; 1.25</p>
  <ol class="ranking">
    <li><span class="rank">01</span><span class="store good">(8) VZaEOSVkef</span><span class="value good">0.2</span></li>
    <li><span class="rank">02</span><span class="store good">(3) PcVKNpUNmj</span><span class="value good">0.2</span></li>
    <li><span class="rank">03</span><span class="store good">(4) RIlyRZsTln</span><span class="value good">0.4</span></li>
    <li><span class="rank">04</span><span class="store good">(9) epINQFtERO</span><span class="value good">0.6</span></li>
    <li><span class="rank">05</span><span class="store good">(3) FbFOzkjSpF</span><span class="value good">0.7</span></li>
    <li><span class="rank">06</span><span class="store good">(7) RdzzkcVqtC</span><span class="value good">0.8</span></li>
    <li><span class="rank">07</span><span class="store good">(1) DiIlXiGkTx</span><span class="value good">0.8</span></li>
    <li><span class="rank">08</span><span class="store good">(1) jxWbwORyVa</span><span class="value good">0.8</span></li>
    <li><span class="rank">09</span><span class="store good">(4) UyzYflMzU</span><span class="value good">0.8</span></li>
    <li><span class="rank">10</span><span class="store good">(7) SCXuIMdjcB</span><span class="value good">1</span></li>
    <li><span class="rank">96</span><span class="store bad">(5) gBeGhPqZNF</span><span class="value bad">9.7</span></li>
    <li><span class="rank">97</span><span class="store bad">(8) gGhhZFlCHP</span><span class="value bad">9.7</span></li>
    <li><span class="rank">98</span><span class="store bad">(9) emavLKfhzN</span><span class="value bad">9.8</span></li>
    <li><span class="rank">99</span><span class="store bad">(7) PyuviZHBxH</span><span class="value bad">9.8</span></li>
    <li><span class="rank">100</span><span class="store bad">(5) LidsyctcWm</span><span class="value bad">9.9</span></li>
  </ol>
</section>

<footer class="site-foot">© Copyright-2018 company Name. All rights reserved.<span class="code">C2</span></footer>
</body>
</html>
```